Breakfast Briefings / Lunch & Learn

I would like to have a double sided flyer size 8x10 to display the breakfast briefing on one side and Lunch & Learn on the other side.

Header on each side to say
2018 Calendar Breakfast Briefing (on the breakfast side)
2018 Calendar Lunch & Learn (on the lunch side)

I have attached a copy of the files we would like to use.

Industry/Entity Type

Learn

Colors

Designer to choose colors to be used in the design.

```html
<!DOCTYPE html>
<html lang="en">
<head>
<meta charset="utf-8">
<title>2018 Calendar – Breakfast Briefing</title>
<link href="https://fonts.googleapis.com/css2?family=Montserrat:wght@500;600;700&family=Oswald:wght@600&display=swap" rel="stylesheet">
<style>
  :root {
    --band-blue: #1e78c8;
    --title-cyan: #6ef5ee;
    --paper: #eceeee;
    --ink: #222;
    --row1: #ff3417;
    --row2: #7cf01a;
    --row3: #4aa6f0;
    --row4: #cc3ed6;
  }
  * { margin: 0; padding: 0; box-sizing: border-box; }
  html, body { width: 960px; height: 1200px; overflow: hidden; }
  body { background: var(--paper); font-family: "Montserrat", sans-serif; }
  .flyer { position: relative; width: 960px; height: 1200px; overflow: hidden;
    background: radial-gradient(ellipse at 50% 60%, #ffffff 0%, #e9ebeb 55%, #dde0e0 100%); }
  .backdrop-icons { position: absolute; left: 0; top: 264px; width: 960px; height: 862px;
    background: radial-gradient(ellipse at 50% 50%, rgba(255,255,255,0) 40%, rgba(190,194,196,0.25) 100%); }
  .header-band { position: absolute; left: 0; top: 32px; width: 960px; height: 232px;
    background: var(--band-blue); text-align: center; }
  .header-title { color: var(--title-cyan); font-weight: 600; font-size: 92px; line-height: 1;
    letter-spacing: 1px; padding-top: 24px; }
  .header-rule { width: 804px; height: 4px; background: var(--title-cyan); margin: 21px auto 0; }
  .header-subtitle { color: #fff; font-weight: 600; font-size: 74px; line-height: 1; margin-top: 12px; }
  .footer-band { position: absolute; left: 0; top: 1126px; width: 960px; height: 74px; background: var(--band-blue); }
  .timeline { position: absolute; left: 0; top: 0; }
  .month { font-family: "Montserrat", sans-serif; font-weight: 500; font-size: 21px; }
  .dept { font-family: "Montserrat", sans-serif; font-weight: 500; font-size: 16px; fill: #fff; text-anchor: middle; }
  .speaker { font-family: "Oswald", sans-serif; font-weight: 600; font-size: 19px; fill: var(--ink); text-anchor: middle; }
  .row1 { fill: var(--row1); } .row2 { fill: var(--row2); } .row3 { fill: var(--row3); } .row4 { fill: var(--row4); }
  .notch { fill: none; stroke: #eef0f0; stroke-width: 5; }
  .brand { position: absolute; right: 30px; top: 1082px; display: flex; align-items: center; gap: 8px; }
  .brand-mark { width: 14px; height: 14px; background: var(--band-blue); }
  .brand-name { font-family: "Montserrat", sans-serif; font-weight: 600; font-size: 22px; color: var(--band-blue); }
</style>
</head>
<body>
<main class="flyer">
  <div class="backdrop-icons" role="img" aria-label="Faint grey business icons: dollar sign, wrench, light bulb, megaphone and team figures"></div>

  <header class="header-band">
    <h1 class="header-title">2018 CALENDAR</h1>
    <div class="header-rule"></div>
    <h2 class="header-subtitle">Breakfast Briefing</h2>
  </header>

  <svg class="timeline" width="960" height="1200" viewBox="0 0 960 1200" aria-label="Monthly briefing timeline">
    <defs>
      <linearGradient id="turn1" gradientUnits="userSpaceOnUse" x1="0" y1="374" x2="0" y2="593">
        <stop offset="0" stop-color="#ff3a14"/><stop offset="0.25" stop-color="#ff8a12"/>
        <stop offset="0.5" stop-color="#f0f514"/><stop offset="1" stop-color="#7cf01a"/>
      </linearGradient>
      <linearGradient id="turn2" gradientUnits="userSpaceOnUse" x1="0" y1="593" x2="0" y2="814">
        <stop offset="0" stop-color="#7cf01a"/><stop offset="0.55" stop-color="#7ff5e6"/>
        <stop offset="1" stop-color="#4aa6f0"/>
      </linearGradient>
      <linearGradient id="row3" gradientUnits="userSpaceOnUse" x1="232" y1="0" x2="716" y2="0">
        <stop offset="0" stop-color="#4aa6f0"/><stop offset="1" stop-color="#3d7cf2"/>
      </linearGradient>
      <linearGradient id="turn3" gradientUnits="userSpaceOnUse" x1="0" y1="814" x2="0" y2="1034">
        <stop offset="0" stop-color="#3d7cf2"/><stop offset="0.45" stop-color="#2434f5"/>
        <stop offset="0.75" stop-color="#8a38f0"/><stop offset="1" stop-color="#cc3ed6"/>
      </linearGradient>
      <linearGradient id="turn4" gradientUnits="userSpaceOnUse" x1="0" y1="1034" x2="0" y2="1150">
        <stop offset="0" stop-color="#d83ec8"/><stop offset="1" stop-color="#ff1a1a"/>
      </linearGradient>
    </defs>

    <g class="ribbon" fill="none" stroke-width="29">
      <path d="M128 374 H716" stroke="#ff3417" stroke-linecap="round"/>
      <path d="M716 374 A109.5 109.5 0 0 1 716 593" stroke="url(#turn1)"/>
      <path d="M716 593 H232" stroke="#7cf01a"/>
      <path d="M232 593 A110.5 110.5 0 0 0 232 814" stroke="url(#turn2)"/>
      <path d="M232 814 H716" stroke="url(#row3)"/>
      <path d="M716 814 A110 110 0 0 1 716 1034" stroke="url(#turn3)"/>
      <path d="M716 1034 H240" stroke="#cc3ed6"/>
      <path d="M240 1034 A116 116 0 0 0 124 1150" stroke="url(#turn4)"/>
    </g>

    <g class="notches">
      <polyline class="notch" points="316,358 330,374 316,390"/>
      <polyline class="notch" points="548,358 562,374 548,390"/>
      <polyline class="notch" points="560,577 546,593 560,609"/>
      <polyline class="notch" points="108,696 122,710 136,696"/>
      <polyline class="notch" points="346,798 360,814 346,830"/>
      <polyline class="notch" points="560,798 574,814 560,830"/>
      <polyline class="notch" points="568,1018 554,1034 568,1050"/>
    </g>

    <g class="stop">
      <text class="month row1" x="130" y="346">MARCH</text>
      <text class="dept" x="222" y="380">FINANCE</text>
      <text class="speaker" x="229" y="411">Ron Calder</text>
    </g>
    <g class="stop">
      <text class="month row1" x="339" y="346">APRIL</text>
      <text class="dept" x="430" y="380">R &amp; D</text>
      <text class="speaker" x="442" y="411">Nick Anastasiou</text>
    </g>
    <g class="stop">
      <text class="month row1" x="571" y="346">MAY</text>
      <text class="dept" x="669" y="380">OPERATIONS</text>
      <text class="speaker" x="658" y="411">Peter Schindler</text>
    </g>

    <g class="stop">
      <text class="month row2" x="205" y="565">AUGUST</text>
      <text class="dept" x="267" y="599">PEPOLE</text>
      <text class="speaker" x="261" y="633">Meera Ghosal</text>
    </g>
    <g class="stop">
      <text class="month row2" x="394" y="565">JULY</text>
      <text class="dept" x="446" y="599">QUALITY</text>
      <text class="speaker" x="445" y="633">Dennis Abramovich</text>
    </g>
    <g class="stop">
      <text class="month row2" x="576" y="565">JUNE</text>
      <text class="dept" x="661" y="599">CLINICAL/REG</text>
      <text class="speaker" x="656" y="634">Brett Glover</text>
    </g>

    <g class="stop">
      <text class="month row3" x="202" y="786">SEPTEMBER</text>
      <text class="dept" x="262" y="820">MARKETING</text>
      <text class="speaker" x="267" y="853">Nitin Tandon</text>
    </g>
    <g class="stop">
      <text class="month row3" x="384" y="786">OCTOBER</text>
      <text class="dept" x="458" y="820">LEGAL</text>
      <text class="speaker" x="446" y="853">Kamal Rahman</text>
    </g>
    <g class="stop">
      <text class="month row3" x="566" y="786">NOVEMBER</text>
      <text class="dept" x="662" y="820">MARKET ACCESS</text>
      <text class="speaker" x="648" y="853">Katrina Neumeister</text>
    </g>

    <g class="stop">
      <text class="month row4" x="197" y="1006">2019 TBD</text>
      <text class="dept" x="239" y="1040">SALES</text>
      <text class="speaker" x="245" y="1075">Joe Alvarez</text>
    </g>
    <g class="stop">
      <text class="month row4" x="373" y="1006">2019 TBD</text>
      <text class="dept" x="418" y="1040">MEDICAL</text>
      <text class="speaker" x="423" y="1075">Daniel Calloway</text>
    </g>
    <g class="stop">
      <text class="month row4" x="571" y="1006">DECEMBER</text>
      <text class="dept" x="613" y="1040">TOS</text>
      <text class="speaker" x="631" y="1075">Clara Smithers</text>
    </g>
  </svg>

  <div class="footer-band"></div>
  <div class="brand">
    <span class="brand-mark"></span>
    <span class="brand-name">Calvessa</span>
  </div>
</main>
</body>
</html>
```